ASL Learning Website Application Pages Redesign

Introduction:
We need a redesign of the internal pages of our website, SignQuiverly.com. The current website design has been in place for many years and is not mobile friendly. We want an updated design that makes the site look cleaner, more professional, and mobile accessible. We are looking for a design that eliminates the clutter on each page, and makes the site simple and easy to use. We will be interested in your design if it is unique and creative. Don't be afraid to completely change the look of the site.

We need the designs sliced up into clean HTML files that are responsive and work well on both mobile and desktop computers. We will implement the PHP needed to make the pages functional.

About Us:
SignQuiverly is a subscription-based website for American Sign Language (ASL) video lessons. The content is for anyone who wishes to learn ASL, regardless of age. It has been designed to instruct Deaf students, parents of Deaf children, and the community-at-large. All lessons are taught by Deaf experts of ASL.

Overview:
The website before log-in does not need any changes. There are five key pages within the internal website (after log-in) that need to be redesigned; they are listed below. Note that some pages (Dictionary and Activity) have multiple sub-pages, so there are about 6-8 pages in total to design, depending on how you decide to approach this (more info in the pages’ respective instruction documents).

The new page designs should retain their existing features, and as stated before, should be mobile friendly. However, you may combine, collapse, or completely change the look of these features. Each page to redesign has a separate instruction document attachment, and screenshots of the current version of the page. Our logo has also been attached. If you want to see the website pages for yourself, you can also go to our website (SignQuiverly.com) and use a free trial to get access to the internal site.

As for design preferences, we want our site to be modern-looking and mature. We’re looking for an inviting, educational style that can attract both high school students and adults. We’re happy with the current font and color scheme, but we’re always open to ideas!

Additional Notes:
- Every page has the same header and footer. You could keep these the same, or change them, based on your discretion.
- Currently, every page also has a breadcrumb. The breadcrumb is unnecessary and you may remove it. However, the “add/remove from favorites” button on the right of the breadcrumb is necessary to keep somewhere on the page.

Pages:
Here’s a list of the five key pages we need redesigned:
- Dashboard
- Dictionary
- Lesson
- Activity
- All Lessons

Each page has its own instruction document. These are attached separately.

Just purchased a $150 for Top designers. I need to give them time to submit their designs . Can I have 7 more days?

Target Market(s)

Deaf students, parents of Deaf children, and the community-at-large interested in learning ASL

Coding

Number of Pages Required

5+ page

Font styles to use
Sans Serif

Requirements
Must have
• Responsive design - the full application experience should be available on mobile devices.
Follow the directions on the design brief.
Nice to have
• Be creative! Please play around with, or even completely change, the look of the site.

```html
<!DOCTYPE html>
<html lang="en">
<head>
<meta charset="utf-8">
<title>SignQuiverly – Activity: Choose the correct sentence</title>
<link href="https://fonts.googleapis.com/css2?family=Barlow:wght@500;600&family=Poppins:wght@400;500;600&family=Open+Sans:wght@400;600&display=swap" rel="stylesheet">
<style>
:root{
  --green:#62a830;
  --green-dark:#579a2a;
  --cream:#fbf3e1;
  --nav:#6a6a6a;
  --ink:#222;
  --text:#444;
  --muted:#666;
  --faint:#eeeeee;
  --field:#f2f2f2;
  --line:#e6e6e6;
}
*{box-sizing:border-box;margin:0;padding:0}
html,body{width:1200px;height:2260px;overflow:hidden;background:#fff}
body{font-family:"Poppins",sans-serif;color:var(--ink);position:relative}

.site-header{display:flex;height:121px}
.brand{width:434px;background:var(--cream);display:flex;align-items:center;padding-left:92px;gap:10px}
.brand-mark{width:18px;height:18px;background:var(--green)}
.brand-name{font:500 40px "Poppins",sans-serif;color:var(--ink);letter-spacing:-1px}
.header-banner{flex:1;background:var(--green);color:#fff;padding:20px 0 0 78px;position:relative}
.header-banner::before{content:"";position:absolute;left:0;top:48px;border:12px solid transparent;border-left-color:var(--cream)}
.banner-title{font:600 21px "Barlow",sans-serif;letter-spacing:-.2px}
.banner-user{font:500 15px "Barlow",sans-serif;margin-top:6px;padding-left:18px}
.banner-user em{font-style:italic}

.main-nav{height:46px;background:var(--nav);display:flex;align-items:center;padding-left:125px;gap:27px}
.main-nav a{font:600 17px "Barlow",sans-serif;color:#fff;text-decoration:none;display:flex;align-items:center;gap:4px}
.caret{width:0;height:0;border:5px solid transparent;border-top-color:#fff;margin-top:5px}

.crumbs{position:absolute;top:209px;left:89px;right:89px;display:flex;align-items:center;font:500 14px "Poppins",sans-serif}
.crumbs span.sep{color:#888;margin:0 10px;font-size:12px}
.crumbs .current{color:var(--green)}
.fav-btn{margin-left:auto;background:#eeeeee;border-radius:2px;padding:9px 16px;font:600 12px "Poppins",sans-serif;letter-spacing:.3px;display:flex;align-items:center;gap:7px}
.divider{position:absolute;top:274px;left:89px;width:1022px;height:1px;background:var(--line)}

.activity-head{position:absolute;top:312px;left:0;width:1200px;text-align:center}
.activity-head h1{font:600 32px "Poppins",sans-serif;letter-spacing:.3px}
.activity-head p{font:400 14px "Poppins",sans-serif;color:var(--muted);margin-top:6px}
.section-title{position:absolute;top:436px;width:1200px;text-align:center;font:500 19px "Poppins",sans-serif;letter-spacing:.3px}

.cards{position:absolute;top:480px;left:89px;width:1022px;display:grid;grid-template-columns:repeat(3,323px);gap:25px 26px}
.card{height:535px;background:#fff;border-radius:10px;box-shadow:0 2px 14px rgba(0,0,0,.07);padding:11px}
.video{height:237px;border-radius:10px;background:linear-gradient(135deg,#e9ecef 0%,#c9d3da 45%,#7ea4c4 70%,#b48a5b 100%);display:flex;align-items:center;justify-content:center}
.card-num{font:600 52px "Poppins",sans-serif;color:var(--faint);margin:8px 0 0 20px;line-height:1;height:48px}
.options{list-style:none;margin:5px 0 0 22px}
.options li{font:400 14.5px "Poppins",sans-serif;color:var(--text);height:26.7px;display:flex;align-items:center;gap:9px}
.options li::before{content:"";width:8px;height:8px;border:2px solid var(--green);border-radius:50%}
.answer-label{font:600 14px "Poppins",sans-serif;margin:14px 0 0 18px}
.answer-field{margin:8px 0 0 18px;width:267px;height:40px;background:var(--field);border-radius:2px;position:relative}
.answer-field::before{content:"";position:absolute;left:20px;top:10px;width:1.5px;height:20px;background:#999}

.submit{position:absolute;top:1638px;left:459px;width:282px;height:45px;background:var(--green);color:#fff;border-radius:2px;font:600 14px "Poppins",sans-serif;letter-spacing:.6px;display:flex;align-items:center;justify-content:center}

.site-footer{position:absolute;top:1791px;left:0;width:1200px;height:469px;border-top:4px solid var(--green);font-family:"Open Sans",sans-serif}
.foot-about{position:absolute;left:89px;top:48px;width:290px}
.foot-brand{display:flex;align-items:center;gap:8px}
.foot-brand .brand-name{font-size:32px}
.foot-brand .brand-mark{width:14px;height:14px}
.foot-about p{font-size:12.5px;color:var(--muted);line-height:25.8px;margin-top:26px}
.vline{position:absolute;top:70px;width:1px;height:200px;background:var(--line)}
.foot-col h3{font:600 20px "Poppins",sans-serif;position:absolute;top:52px}
.foot-links{position:absolute;list-style:none;top:92px}
.foot-links li{font-size:12.5px;color:var(--muted);height:26px}
.contact{position:absolute;left:818px;top:92px;list-style:none}
.contact li{font-size:12.5px;color:var(--muted);height:39px;display:flex;gap:10px}
.contact svg{flex:none;margin-top:2px}
.foot-bottom{position:absolute;left:89px;top:377px;width:1022px;border-top:1px solid #ddd;display:flex;align-items:center;justify-content:space-between;height:86px}
.foot-bottom small{font-size:12.5px;color:var(--muted)}
.social{display:flex;gap:12px}
.social span{width:34px;height:34px;border:1px solid #cfcfcf;border-radius:50%}
</style>
</head>
<body>

<header class="site-header">
  <div class="brand"><span class="brand-mark"></span><span class="brand-name">SignQuiverly</span></div>
  <div class="header-banner">
    <div class="banner-title">LEARN ASL THROUGH VIDEO LESSONS ONLINE</div>
    <div class="banner-user">You are currently logged in as: <em>jmarlowe</em></div>
  </div>
</header>
<nav class="main-nav">
  <a>Dashboard</a><a>Lessons<i class="caret"></i></a><a>Lesson List</a><a>Dictionary</a>
  <a>Handshapes<i class="caret"></i></a><a>Locations<i class="caret"></i></a><a>Update Account<i class="caret"></i></a><a>Logout</a>
</nav>

<div class="crumbs">
  <span>SignQuiverly</span><span class="sep">›</span><span>Dashboard</span><span class="sep">›</span>
  <span class="current">Activity: Choose the correct sentence</span>
  <span class="fav-btn"><svg width="12" height="12" viewBox="0 0 12 12"><path d="M6 0v12M0 6h12" stroke="#222" stroke-width="2"/></svg>ADD TO FAVORITES</span>
</div>
<div class="divider"></div>

<div class="activity-head">
  <h1>Acticity choose the correct sentence</h1>
  <p>After viewing the video, choose the correct word or phrase</p>
</div>
<div class="section-title">Choose the correct sentence</div>

<main class="cards">
  <article class="card"><div class="video" role="img" aria-label="Video of an instructor signing the sentence"><svg width="48" height="48" viewBox="0 0 48 48"><circle cx="24" cy="24" r="24" fill="rgba(0,0,0,.3)"/><path d="M20 16l12 8-12 8z" fill="#fff"/></svg></div>
    <div class="card-num">01</div>
    <ul class="options"><li>I am fine.</li><li>You are doing fine.</li><li>See you later.</li><li>How are you feeling?</li></ul>
    <div class="answer-label">Answer:</div><div class="answer-field"></div></article>
  <article class="card"><div class="video" role="img" aria-label="Video of an instructor signing the sentence"><svg width="48" height="48" viewBox="0 0 48 48"><circle cx="24" cy="24" r="24" fill="rgba(0,0,0,.3)"/><path d="M20 16l12 8-12 8z" fill="#fff"/></svg></div>
    <div class="card-num">02</div>
    <ul class="options"><li>You are nice.</li><li>How are you feeling?</li><li>Have a great day!</li><li>I am feeling good.</li></ul>
    <div class="answer-label">Answer:</div><div class="answer-field"></div></article>
  <article class="card"><div class="video" role="img" aria-label="Video of an instructor signing the sentence"><svg width="48" height="48" viewBox="0 0 48 48"><circle cx="24" cy="24" r="24" fill="rgba(0,0,0,.3)"/><path d="M20 16l12 8-12 8z" fill="#fff"/></svg></div>
    <div class="card-num">03</div>
    <ul class="options"><li>I like evenings.</li><li>I like mornings.</li><li>I don't like mornings.</li><li>Do you like afternoons?</li></ul>
    <div class="answer-label">Answer:</div><div class="answer-field"></div></article>
  <article class="card"><div class="video" role="img" aria-label="Video of an instructor signing the sentence"><svg width="48" height="48" viewBox="0 0 48 48"><circle cx="24" cy="24" r="24" fill="rgba(0,0,0,.3)"/><path d="M20 16l12 8-12 8z" fill="#fff"/></svg></div>
    <div class="card-num">04</div>
    <ul class="options"><li>Nice to meet you.</li><li>Nice to see you.</li><li>Good morning to you.</li><li>Bye for now.</li></ul>
    <div class="answer-label">Answer:</div><div class="answer-field"></div></article>
  <article class="card"><div class="video" role="img" aria-label="Video of an instructor signing the sentence"><svg width="48" height="48" viewBox="0 0 48 48"><circle cx="24" cy="24" r="24" fill="rgba(0,0,0,.3)"/><path d="M20 16l12 8-12 8z" fill="#fff"/></svg></div>
    <div class="card-num">05</div>
    <ul class="options"><li>What is your name?</li><li>My name is Bob.</li><li>Good morning.</li><li>Do you have a name?</li></ul>
    <div class="answer-label">Answer:</div><div class="answer-field"></div></article>
  <article class="card"><div class="video" role="img" aria-label="Video of an instructor signing the sentence"><svg width="48" height="48" viewBox="0 0 48 48"><circle cx="24" cy="24" r="24" fill="rgba(0,0,0,.3)"/><path d="M20 16l12 8-12 8z" fill="#fff"/></svg></div>
    <div class="card-num">06</div>
    <ul class="options"><li>I am fine.</li><li>You are doing fine.</li><li>See you later.</li><li>How are you feeling?</li></ul>
    <div class="answer-label">Answer:</div><div class="answer-field"></div></article>
</main>

<div class="submit">I'M DONE, SUBMIT MY ANSWERS</div>

<footer class="site-footer">
  <div class="foot-about">
    <div class="foot-brand"><span class="brand-mark"></span><span class="brand-name">SignQuiverly</span></div>
    <p>SignQuiverly is a subscription based website for American Sign Language (ASL) video lessons. The content is for anyone who wishes to learn ASL, regardless of age. It has been designed to instruct Deaf students, parents of Deaf children, and the community-at-large. You may cancel your subscription at any time. All lessons are taught by Deaf experts of ASL.</p>
  </div>
  <div class="vline" style="left:395px"></div>
  <div class="foot-col"><h3 style="left:436px">Quick Links</h3></div>
  <ul class="foot-links" style="left:436px"><li>Home</li><li>Try it Free</li><li>Contact Us</li></ul>
  <ul class="foot-links" style="left:609px"><li>Group Rate Form</li><li>Teacher's Guide</li><li>Gift Certificates</li><li>FAQs</li><li>Privacy Policy</li></ul>
  <div class="vline" style="left:791px"></div>
  <div class="foot-col"><h3 style="left:818px">Contact Us</h3></div>
  <ul class="contact">
    <li><svg width="10" height="14" viewBox="0 0 10 14"><path d="M5 0a5 5 0 015 5c0 4-5 9-5 9S0 9 0 5a5 5 0 015-5z" fill="#62a830"/><circle cx="5" cy="5" r="2" fill="#fff"/></svg>PO Box 50812, Cedar Falls, MI 48000</li>
    <li><svg width="12" height="12" viewBox="0 0 12 12"><path d="M2 0l2.5 3-1.5 1.5a7 7 0 004.5 4.5L9 7.5l3 2.5-1.5 2C5 12 0 7 0 1.5z" fill="#62a830"/></svg>(555) 014-2290</li>
    <li><svg width="12" height="10" viewBox="0 0 12 10"><rect width="12" height="10" fill="#62a830"/><path d="M0 1l6 4 6-4" stroke="#fff" fill="none"/></svg>info@signquiverly.com</li>
  </ul>
  <div class="foot-bottom">
    <small>Copyrights © 2021, SignQuiverly. All rights reserved. Terms &amp; Conditions</small>
    <div class="social"><span></span><span></span><span></span><span></span><span></span></div>
  </div>
</footer>

</body>
</html>
```